We need a Photoshop specialist to design our outdoor billboard sign.

We need someone to design a billboard for us that will measure 8 feet wide 4 feet tall the Billboard needs to represent our company which is Brindle Hollow Fitters and advertised that we do home theater installation home security and surveillance home automation and TV installation. Visit our website for more info BrindleHollowFitters.example

Target Market(s)

homeowners in the area

Industry/Entity Type

It Company

Font styles to use
Sans Serif

Requirements
Must have
• company logo, pictures that represent our services, a list of our services, phone number, website address.

```html
<!DOCTYPE html>
<html lang="en">
<head>
<meta charset="utf-8">
<title>Brindle Hollow Fitters – Billboard</title>
<link href="https://fonts.googleapis.com/css2?family=PT+Sans:wght@400;700&display=swap" rel="stylesheet">
<style>
  :root {
    --brown: #8b5a2e;
    --brown-dark: #4a2a14;
    --red: #c1272d;
    --frame: #8a5526;
    --panel: rgba(214, 210, 206, 0.55);
    --white: #ffffff;
  }
  * { margin: 0; padding: 0; box-sizing: border-box; }
  html, body { width: 1200px; height: 600px; overflow: hidden; background: var(--white); }
  .billboard {
    position: relative; width: 1200px; height: 600px; overflow: hidden;
    font-family: "PT Sans", sans-serif;
    background: var(--white);
  }
  .backdrop {
    position: absolute; inset: 0;
    background:
      radial-gradient(ellipse 520px 150px at 330px 40px, rgba(242,106,27,0.85), transparent 70%),
      radial-gradient(ellipse 420px 140px at 820px 30px, rgba(224,58,18,0.8), transparent 70%),
      radial-gradient(ellipse 380px 160px at 1080px 120px, rgba(242,106,27,0.7), transparent 70%),
      radial-gradient(ellipse 300px 120px at 560px 190px, rgba(251,209,168,0.7), transparent 70%),
      radial-gradient(ellipse 500px 120px at 300px 260px, rgba(251,209,168,0.55), transparent 70%),
      linear-gradient(180deg, #fde2cc 0%, #fff 55%);
  }
  .photo { position: absolute; border: 3px solid var(--frame); }
  .panel { position: absolute; background: var(--panel); }
  .service { position: absolute; line-height: 23px; }
  .service h2 { font-weight: 400; font-size: 23px; color: var(--brown); line-height: 26px; }
  .service ul { list-style: none; font-size: 19px; color: var(--red); }
  .service p { font-size: 19px; color: var(--red); }

  .brand {
    position: absolute; left: 690px; top: 40px; width: 490px;
    text-align: center; color: var(--brown-dark);
    font-weight: 700; font-size: 60px; line-height: 62px; letter-spacing: 2px;
    text-transform: uppercase;
  }

  .footer-bar {
    position: absolute; left: 229px; top: 554px; width: 971px; height: 46px;
    background: linear-gradient(180deg, #7a4520 0%, #5a2e12 55%, #6e3d1b 100%);
  }
  .footer-brand {
    position: absolute; left: 8px; top: 566px; width: 214px;
    color: var(--brown-dark); white-space: nowrap;
    font-weight: 700; font-size: 15px; line-height: 20px; text-transform: uppercase;
  }
  .contact { position: absolute; display: flex; align-items: center; color: var(--white); }
  .contact svg { margin-right: 10px; }
  .phone { left: 288px; top: 557px; font-size: 33px; }
  .web { left: 676px; top: 562px; font-size: 22px; letter-spacing: 1.5px; }
</style>
</head>
<body>
<main class="billboard">
  <div class="backdrop" role="img" aria-label="Soft orange and red flame smoke wash across the top"></div>

  <div class="brand">Brindle Hollow<br>Fitters</div>

  <!-- TV installation -->
  <div class="panel" style="left:240px;top:57px;width:190px;height:112px"></div>
  <div class="photo" role="img" aria-label="Living room with wall-mounted flat screen TV"
       style="left:18px;top:54px;width:222px;height:125px;background:linear-gradient(135deg,#e9e6e2,#9a948f 55%,#3b3b3e)"></div>
  <section class="service" style="left:252px;top:60px">
    <h2>TV Installation</h2>
    <ul style="margin-left:36px"><li>Table Top</li><li>On Wall</li><li>Fire Place</li></ul>
  </section>

  <!-- Surround sound -->
  <div class="panel" style="left:288px;top:224px;width:322px;height:110px"></div>
  <div class="photo" role="img" aria-label="Black home theater speaker system"
       style="left:65px;top:214px;width:223px;height:127px;background:linear-gradient(180deg,#ffffff,#d9d9db 60%,#2a2a2e)"></div>
  <section class="service" style="left:293px;top:227px">
    <h2>Surround Sound Installation</h2>
    <ul style="margin-left:34px"><li>Basic Home Theater</li><li>5.1 Surround</li><li>7.1 Surround</li></ul>
  </section>

  <!-- Home theater -->
  <div class="panel" style="left:646px;top:234px;width:540px;height:114px"></div>
  <div class="photo" role="img" aria-label="Home cinema room with curtains, screen and AV equipment"
       style="left:664px;top:230px;width:224px;height:132px;background:linear-gradient(180deg,#7a4a1c,#b07a32 45%,#2c1a0c)"></div>
  <section class="service" style="left:896px;top:240px">
    <h2>Home Theater Installation</h2>
    <p style="margin-left:46px">Complete turnkey home<br>theater packages Starting<br>at only $4999.</p>
  </section>

  <!-- Surveillance home automation -->
  <div class="panel" style="left:240px;top:370px;width:360px;height:120px"></div>
  <div class="photo" role="img" aria-label="Modern kitchen with smartphone home automation app"
       style="left:16px;top:367px;width:224px;height:128px;background:linear-gradient(135deg,#eef1f4,#a8b4bf 60%,#5e6f80)"></div>
  <div role="img" aria-label="Smartphone showing automation controls"
       style="position:absolute;left:170px;top:396px;width:62px;height:126px;border:2px solid var(--red);border-radius:6px;background:linear-gradient(180deg,#f4f6f8,#7d9ab3)"></div>
  <section class="service" style="left:250px;top:363px">
    <h2>Surveillance Home Automation</h2>
    <p style="margin-left:26px">Mobile automation turns<br>your home into a play button.<br>Wireless control over your<br>home elements with ease.</p>
  </section>

  <!-- Home security -->
  <div class="panel" style="left:586px;top:408px;width:572px;height:110px"></div>
  <div class="photo" role="img" aria-label="Hand holding phone with security app in front of a house"
       style="left:599px;top:404px;width:226px;height:127px;background:linear-gradient(135deg,#9fbcd6,#c9b08a 50%,#6a8a3e)"></div>
  <section class="service" style="left:842px;top:410px">
    <h2>Home Security</h2>
    <p style="margin-left:18px">Real time wireless security<br>applications give you security<br>monitoring and options</p>
  </section>

  <!-- Footer -->
  <div class="footer-brand">Brindle Hollow Fitters</div>
  <div class="footer-bar"></div>
  <div class="contact phone">
    <svg width="32" height="32" viewBox="0 0 32 32" aria-hidden="true">
      <circle cx="16" cy="16" r="14" fill="none" stroke="#fff" stroke-width="2.5"/>
      <path d="M11 8c1 0 2 2 2.6 3.4.4.9-1.4 1.9-1.2 2.6.6 2 2.4 3.9 4.4 4.6.7.3 1.8-1.5 2.6-1.1C20.8 18 23 19 23 20c0 1.5-2 3-3.5 3C14 23 9 18 9 12.5 9 10 10 8 11 8z" fill="#fff"/>
    </svg>
    (555)014-2277
  </div>
  <div class="contact web">
    <svg width="36" height="36" viewBox="0 0 36 36" aria-hidden="true">
      <circle cx="18" cy="18" r="15" fill="none" stroke="#fff" stroke-width="2"/>
      <ellipse cx="18" cy="18" rx="7" ry="15" fill="none" stroke="#fff" stroke-width="1.5"/>
      <line x1="3" y1="18" x2="33" y2="18" stroke="#fff" stroke-width="1.5"/>
      <line x1="6" y1="10" x2="30" y2="10" stroke="#fff" stroke-width="1.5"/>
      <line x1="6" y1="26" x2="30" y2="26" stroke="#fff" stroke-width="1.5"/>
    </svg>
    www.BrindleHollowFitters.example
  </div>
</main>
</body>
</html>
```